Photoshop Design

Hi, you did a project for me a while ago as per the below description. Can you do the same again with this screen shot?
"We have a charting software application and we are in the process of upgrading our marketing.
We need our application charting screen re-created in photoshop with all components on separate layers so we can tinker with them later such as highlight particular components we are discussing and the likes.
We need the native photoshop file as the project output"
Target Market(s)
Myself
Requirements
Must have
- Look like the sample provided with layers for later editing.

```html
<!DOCTYPE html>
<html lang="en">
<head>
<meta charset="utf-8">
<title>Charting Dashboard</title>
<link rel="stylesheet" href="https://fonts.googleapis.com/css2?family=Roboto:wght@300;400;500&family=Roboto+Condensed:wght@400&family=Share+Tech+Mono&display=swap">
<style>
  :root {
    --bg: #2a2a2a;
    --top-strip: #ffffff;
    --panel: #303030;
    --panel-low: #2e2e2e;
    --plot: #121212;
    --plot-right: #15191c;
    --band: #172f38;
    --band-right: #1b3542;
    --grid: #4a4a4a;
    --blue: #2a8fd8;
    --sky: #29a9e6;
    --cyan: #4fc3f0;
    --green: #2fb24a;
    --btn-green: #1c9a48;
    --magenta: #e0207e;
    --red: #e42a2a;
    --yellow: #f5e80c;
    --white: #f2f2f2;
    --label: #c8c8c8;
    --dim: #9a9a9a;
    --dial: #1c1c1c;
    --dial-inner: #262626;
    --lcd: #2c2c2c;
    --btn: #353535;
    --btn-dark: #242424;
    --sidebar: #2f2f2f;
  }
  * { margin: 0; padding: 0; box-sizing: border-box; }
  html, body { width: 1200px; height: 675px; overflow: hidden; background: var(--bg); }
  body { position: relative; font-family: "Roboto", sans-serif; color: var(--white); }

  .top-strip { position: absolute; left: 0; top: 0; width: 1200px; height: 20px; background: var(--top-strip); }

  .main-panel { position: absolute; left: 29px; top: 48px; width: 1035px; height: 627px; background: var(--panel); }
  .chart-panel { position: absolute; left: 29px; top: 242px; width: 1035px; height: 433px; background: var(--panel-low); border-top: 1px solid #3a3a3a; }

  .sensor-box { position: absolute; left: 42px; top: 106px; width: 210px; height: 80px; background: #232323; border-radius: 10px; }
  .sensor-title { position: absolute; left: 98px; top: 86px; font-size: 16px; color: var(--label); letter-spacing: .5px; }
  .sensor-lcd { position: absolute; left: 50px; top: 116px; width: 170px; height: 60px; background: var(--lcd); border-radius: 3px; }
  .sensor-value { position: absolute; left: 96px; top: 118px; font-size: 43px; font-weight: 400; color: #4a86c8; letter-spacing: 1px; }

  .dash-svg { position: absolute; left: 0; top: 0; }

  .sidebar { position: absolute; left: 1070px; top: 22px; width: 100px; height: 280px; background: var(--sidebar); }
  .sidebar-low { position: absolute; left: 1070px; top: 573px; width: 100px; height: 102px; background: var(--sidebar); }
  .btn { position: absolute; left: 1075px; width: 90px; height: 40px; background: var(--btn); display: flex; align-items: center; justify-content: center; text-align: center; font-family: "Roboto Condensed", sans-serif; font-size: 13px; line-height: 1.2; color: var(--white); }
  .btn--active { background: var(--btn-green); }
  .btn--tall { height: 50px; }
  .btn--disabled { background: var(--btn-dark); color: #8a8a8a; }

  .svg-text { font-family: "Roboto", sans-serif; }
  .lcd-text { font-family: "Share Tech Mono", monospace; }
</style>
</head>
<body>
  <div class="top-strip"></div>
  <div class="main-panel"></div>
  <div class="chart-panel"></div>

  <div class="sensor-box"></div>
  <div class="sensor-lcd"></div>
  <div class="sensor-title">SENSOR</div>
  <div class="sensor-value">839.0</div>

  <svg class="dash-svg" width="1200" height="675" viewBox="0 0 1200 675" xmlns="http://www.w3.org/2000/svg">
    <defs>
      <path id="tick-arc" d="M -53.74 53.74 A 76 76 0 1 1 53.74 53.74" fill="none"/>
    </defs>

    <!-- Pressure gauge -->
    <g class="gauge gauge--pressure" transform="translate(310 152)">
      <circle r="92" fill="var(--dial)"/>
      <circle r="60" fill="var(--dial-inner)"/>
      <path d="M -45.25 45.25 A 64 64 0 1 1 60.5 -20.8" fill="none" stroke="var(--sky)" stroke-width="8"/>
      <path d="M 0 -72 A 72 72 0 0 1 66.5 -27.6" fill="none" stroke="var(--green)" stroke-width="5"/>
      <path d="M 48.9 22.8 A 54 54 0 0 1 40.1 36.1" fill="none" stroke="var(--red)" stroke-width="3"/>
      <use href="#tick-arc" stroke="var(--white)" stroke-width="5" stroke-dasharray="1 7.953" stroke-dashoffset="0.5"/>
      <use href="#tick-arc" stroke="var(--white)" stroke-width="8" stroke-dasharray="1.8 42.97" stroke-dashoffset="0.9"/>
      <g class="svg-text" font-size="7" fill="var(--white)" text-anchor="middle">
        <text transform="rotate(-135)" y="-84">0</text>
        <text transform="rotate(-101.25)" y="-84">138</text>
        <text transform="rotate(-67.5)" y="-84">275</text>
        <text transform="rotate(-33.75)" y="-84">413</text>
        <text transform="rotate(0)" y="-84">550</text>
        <text transform="rotate(33.75)" y="-84">688</text>
        <text transform="rotate(67.5)" y="-84">825</text>
        <text transform="rotate(101.25)" y="-84">963</text>
        <text transform="rotate(135)" y="-84">1100</text>
      </g>
      <polygon points="-2,-3 56,-12 58,-10 2,4" fill="#8a8a8a"/>
      <circle r="11" fill="#555" stroke="#e0e0e0" stroke-width="1.8"/>
      <text class="svg-text" y="35" font-size="12" fill="var(--dim)" text-anchor="middle">psi</text>
      <rect x="-24" y="42" width="48" height="15" fill="#2a2a2a"/>
      <text class="lcd-text" x="8" y="54" font-size="11" fill="var(--magenta)" text-anchor="middle" letter-spacing="1">30.1</text>
      <text class="svg-text" y="68" font-size="7.5" fill="var(--dim)" text-anchor="middle">deg C</text>
    </g>

    <!-- Change gauge -->
    <g class="gauge gauge--change" transform="translate(502 146)">
      <circle r="90" fill="var(--dial)"/>
      <circle r="64" fill="var(--dial-inner)"/>
      <use href="#tick-arc" stroke="var(--white)" stroke-width="5" stroke-dasharray="1 7.953" stroke-dashoffset="0.5"/>
      <use href="#tick-arc" stroke="var(--cyan)" stroke-width="9" stroke-dasharray="1.8 42.97" stroke-dashoffset="0.9"/>
      <path d="M -4.6 -75.9 A 76 76 0 0 1 4.6 -75.9" fill="none" stroke="var(--green)" stroke-width="9"/>
      <g class="svg-text" font-size="7" fill="var(--white)" text-anchor="middle">
        <text transform="rotate(-135)" y="-84">-70</text>
        <text transform="rotate(-101.25)" y="-84">-55</text>
        <text transform="rotate(-67.5)" y="-84">-40</text>
        <text transform="rotate(-33.75)" y="-84">-25</text>
        <text transform="rotate(0)" y="-84">-10</text>
        <text transform="rotate(33.75)" y="-84">5</text>
        <text transform="rotate(67.5)" y="-84">20</text>
        <text transform="rotate(101.25)" y="-84">35</text>
        <text transform="rotate(135)" y="-84">50</text>
      </g>
      <text class="svg-text" y="-44" font-size="5.5" fill="var(--dim)" text-anchor="middle">TEST SPEC</text>
      <text class="svg-text" y="-22" font-size="15" fill="var(--label)" text-anchor="middle" letter-spacing=".5">CHANGE</text>
      <rect x="-49" y="-16" width="98" height="33" fill="var(--lcd)"/>
      <text class="lcd-text" x="22" y="10" font-size="25" fill="var(--white)" text-anchor="middle" letter-spacing="3">-5.3</text>
      <text class="svg-text" y="31" font-size="13" fill="var(--dim)" text-anchor="middle">psi</text>
    </g>

    <!-- Rate gauge -->
    <g class="gauge gauge--rate" transform="translate(691 146)">
      <circle r="90" fill="var(--dial)"/>
      <circle r="64" fill="var(--dial-inner)"/>
      <use href="#tick-arc" stroke="var(--white)" stroke-width="5" stroke-dasharray="1 7.953" stroke-dashoffset="0.5"/>
      <use href="#tick-arc" stroke="var(--cyan)" stroke-width="9" stroke-dasharray="1.8 42.97" stroke-dashoffset="0.9"/>
      <path d="M -4.6 -75.9 A 76 76 0 0 1 4.6 -75.9" fill="none" stroke="var(--green)" stroke-width="9"/>
      <polygon points="0,-60 -4,-52 4,-52" fill="#bdbdbd"/>
      <g class="svg-text" font-size="7" fill="var(--white)" text-anchor="middle">
        <text transform="rotate(-135)" y="-84">-40</text>
        <text transform="rotate(-101.25)" y="-84">-33</text>
        <text transform="rotate(-67.5)" y="-84">-25</text>
        <text transform="rotate(-33.75)" y="-84">-18</text>
        <text transform="rotate(0)" y="-84">-10</text>
        <text transform="rotate(33.75)" y="-84">-3</text>
        <text transform="rotate(67.5)" y="-84">5</text>
        <text transform="rotate(101.25)" y="-84">13</text>
        <text transform="rotate(135)" y="-84">20</text>
      </g>
      <text class="svg-text" y="-41" font-size="5.5" fill="var(--dim)" text-anchor="middle">TEST SPEC</text>
      <text class="svg-text" y="-19" font-size="15" fill="var(--label)" text-anchor="middle" letter-spacing=".5">RATE</text>
      <rect x="-49" y="-14" width="98" height="33" fill="var(--lcd)"/>
      <text class="lcd-text" x="22" y="13" font-size="25" fill="var(--white)" text-anchor="middle" letter-spacing="3">-8.1</text>
      <text class="svg-text" y="34" font-size="13" fill="var(--dim)" text-anchor="middle" letter-spacing=".5">psi / min</text>
    </g>

    <!-- Trend gauge -->
    <g class="gauge gauge--trend" transform="translate(880 146)">
      <circle r="90" fill="var(--dial)"/>
      <circle r="64" fill="var(--dial-inner)"/>
      <use href="#tick-arc" stroke="var(--white)" stroke-width="5" stroke-dasharray="1 7.953" stroke-dashoffset="0.5"/>
      <use href="#tick-arc" stroke="var(--cyan)" stroke-width="9" stroke-dasharray="1.8 42.97" stroke-dashoffset="0.9"/>
      <polygon points="0,-62 -4,-54 4,-54" fill="#bdbdbd"/>
      <g class="svg-text" font-size="7" fill="var(--white)" text-anchor="middle">
        <text transform="rotate(-135)" y="-84">-100</text>
        <text transform="rotate(-101.25)" y="-84">-75</text>
        <text transform="rotate(-67.5)" y="-84">-50</text>
        <text transform="rotate(-33.75)" y="-84">-25</text>
        <text transform="rotate(0)" y="-84">0</text>
        <text transform="rotate(33.75)" y="-84">25</text>
        <text transform="rotate(67.5)" y="-84">50</text>
        <text transform="rotate(101.25)" y="-84">75</text>
        <text transform="rotate(135)" y="-84">100</text>
      </g>
      <text class="svg-text" y="-42" font-size="5.5" fill="var(--dim)" text-anchor="middle">TEST SPEC</text>
      <text class="svg-text" y="-20" font-size="15" fill="var(--label)" text-anchor="middle" letter-spacing=".5">TREND</text>
      <rect x="-48" y="-15" width="96" height="32" fill="var(--lcd)"/>
      <text class="lcd-text" y="7" font-size="15" fill="var(--white)" text-anchor="middle" letter-spacing=".5">Improving</text>
    </g>

    <!-- Hold gauge -->
    <g class="hold-gauge">
      <rect x="978" y="58" width="85" height="174" rx="8" fill="#1a1a1a"/>
      <rect x="1006" y="70" width="10" height="130" fill="#3a3a3a"/>
      <rect x="1006" y="126" width="10" height="74" fill="var(--sky)"/>
      <line x1="1016" y1="70" x2="1016" y2="200" stroke="var(--white)" stroke-width="1"/>
      <g stroke="var(--white)" stroke-width="1">
        <line x1="1016" y1="71" x2="1021" y2="71"/><line x1="1016" y1="104" x2="1021" y2="104"/>
        <line x1="1016" y1="136" x2="1021" y2="136"/><line x1="1016" y1="167" x2="1021" y2="167"/>
        <line x1="1016" y1="200" x2="1021" y2="200"/>
      </g>
      <g class="svg-text" font-size="7" fill="var(--white)">
        <text x="1023" y="74">100</text><text x="1023" y="107">75</text>
        <text x="1023" y="139">52</text><text x="1023" y="170">25</text>
        <text x="1023" y="203">0</text>
      </g>
      <text class="svg-text" x="1021" y="222" font-size="14" fill="var(--label)" text-anchor="middle" letter-spacing="1.5">HOLD %</text>
    </g>

    <!-- Chart -->
    <g class="chart">
      <rect x="74" y="251" width="584" height="381" fill="var(--plot)"/>
      <rect x="658" y="251" width="362" height="381" fill="var(--plot-right)"/>
      <rect x="74" y="337" width="584" height="157" fill="var(--band)"/>
      <rect x="658" y="337" width="362" height="157" fill="var(--band-right)"/>
      <rect x="658" y="251" width="362" height="15" fill="#1468a8"/>
      <rect x="659" y="266" width="360" height="366" fill="none" stroke="#1d5f8f" stroke-width="1.5"/>

      <g stroke="var(--grid)" stroke-width=".7" stroke-dasharray="3 3">
        <line x1="142" y1="251" x2="142" y2="632"/><line x1="322" y1="251" x2="322" y2="632"/>
        <line x1="502" y1="251" x2="502" y2="632"/><line x1="682" y1="266" x2="682" y2="632"/>
        <line x1="862" y1="266" x2="862" y2="632"/>
        <line x1="74" y1="290" x2="1020" y2="290"/><line x1="74" y1="326" x2="1020" y2="326"/>
        <line x1="74" y1="362.5" x2="1020" y2="362.5"/><line x1="74" y1="399" x2="1020" y2="399"/>
        <line x1="74" y1="436" x2="1020" y2="436"/><line x1="74" y1="472" x2="1020" y2="472"/>
        <line x1="74" y1="509" x2="1020" y2="509"/><line x1="74" y1="545" x2="1020" y2="545"/>
        <line x1="74" y1="581.6" x2="1020" y2="581.6"/><line x1="74" y1="618" x2="1020" y2="618"/>
      </g>

      <!-- Left temperature axis -->
      <g stroke="var(--magenta)" stroke-width="1">
        <line x1="70" y1="290" x2="74" y2="290"/><line x1="70" y1="362.5" x2="74" y2="362.5"/>
        <line x1="70" y1="436" x2="74" y2="436"/><line x1="70" y1="509" x2="74" y2="509"/>
        <line x1="70" y1="581.6" x2="74" y2="581.6"/>
      </g>
      <g class="svg-text" font-size="11" fill="var(--magenta)" text-anchor="end">
        <text x="67" y="294">30</text><text x="67" y="366.5">25</text>
        <text x="67" y="440">20</text><text x="67" y="513">15</text><text x="67" y="585.6">10</text>
      </g>
      <text class="svg-text" transform="translate(44 440) rotate(-90)" font-size="11" fill="var(--magenta)" text-anchor="middle">Temperature</text>

      <!-- Right pressure axis -->
      <line x1="1020" y1="251" x2="1020" y2="632" stroke="var(--blue)" stroke-width="1.2"/>
      <path d="M1020 628 h4 M1020 621 h6 M1020 614 h4 M1020 606 h4 M1020 598 h4 M1020 590 h6 M1020 582 h4 M1020 574 h4 M1020 566 h4 M1020 558 h6 M1020 550 h4 M1020 542 h4 M1020 534 h4 M1020 527 h6 M1020 519 h4 M1020 511 h4 M1020 503 h4 M1020 495 h6 M1020 487 h4 M1020 479 h4 M1020 471 h4 M1020 463 h6 M1020 455 h4 M1020 447 h4 M1020 440 h4 M1020 432 h6 M1020 424 h4 M1020 416 h4 M1020 408 h4 M1020 400 h6 M1020 392 h4 M1020 384 h4 M1020 376 h4 M1020 368 h6 M1020 360 h4 M1020 353 h4 M1020 345 h4 M1020 337 h6 M1020 329 h4 M1020 321 h4 M1020 313 h4 M1020 305 h6 M1020 297 h4 M1020 289 h4 M1020 281 h4 M1020 274 h6 M1020 266 h4 M1020 258 h4" stroke="var(--blue)" stroke-width=".8"/>
      <g class="svg-text" font-size="8.5" fill="var(--blue)">
        <text x="1028" y="277">1200</text><text x="1028" y="308">1100</text>
        <text x="1028" y="340">1000</text><text x="1028" y="371">900</text>
        <text x="1028" y="403">800</text><text x="1028" y="434">700</text>
        <text x="1028" y="466">600</text><text x="1028" y="498">500</text>
        <text x="1028" y="529">400</text><text x="1028" y="561">300</text>
        <text x="1028" y="592">200</text><text x="1028" y="624">100</text>
      </g>

      <!-- Time axis -->
      <path d="M142 632 v5 M322 632 v5 M502 632 v5 M682 632 v5 M862 632 v5 M178 632 v3 M214 632 v3 M250 632 v3 M286 632 v3 M358 632 v3 M394 632 v3 M430 632 v3 M466 632 v3 M538 632 v3 M574 632 v3 M610 632 v3 M646 632 v3 M718 632 v3 M754 632 v3 M790 632 v3 M826 632 v3 M898 632 v3 M934 632 v3 M970 632 v3 M1006 632 v3" stroke="#8a8a8a" stroke-width=".8"/>
      <g class="svg-text" font-size="10" fill="var(--label)" text-anchor="middle">
        <text x="142" y="650">22:04:30</text><text x="322" y="650">22:05:00</text>
        <text x="502" y="650">22:05:30</text><text x="682" y="650">22:06:00</text>
        <text x="862" y="650">22:06:30</text>
      </g>
      <polygon points="868,639 864,645 872,645" fill="#f39a1e"/>

      <!-- Temperature line -->
      <path d="M88 293 L392 293 Q405 293 412 290 L422 288 L700 289 L884 291" fill="none" stroke="var(--magenta)" stroke-width="2.2"/>

      <!-- Pressure line -->
      <path d="M370 632 L374 620 L378 598 L382 590 L388 560 L392 520 L396 480 L400 450 L402 430 L406 422 L408 410 L410 392 L412 383 L500 384 L658 385 L766 386" fill="none" stroke="var(--sky)" stroke-width="2.4" stroke-linejoin="round"/>
      <line x1="766" y1="385.5" x2="870" y2="385.5" stroke="var(--green)" stroke-width="3"/>
      <line x1="876" y1="386" x2="1020" y2="386" stroke="var(--green)" stroke-width="1.8" stroke-dasharray="9 7"/>
      <circle cx="766" cy="385.5" r="3.5" fill="var(--blue)"/>
      <circle cx="870" cy="385.5" r="3.5" fill="var(--blue)"/>

      <g class="svg-text" font-size="13" fill="var(--blue)" text-anchor="middle">
        <text x="636" y="361">P1</text><text x="636" y="380">844.3</text>
        <text x="744" y="363">P2</text><text x="744" y="380">841.4</text>
        <text x="851" y="363">P3</text><text x="851" y="380">839.0</text>
      </g>

      <!-- Start marker -->
      <path d="M294 593 h70 a3 3 0 0 1 3 3 v19 a3 3 0 0 1 -3 3 h-36 l-6 7 l-6 -7 h-22 a3 3 0 0 1 -3 -3 v-19 a3 3 0 0 1 3 -3 z" fill="var(--yellow)"/>
      <text class="svg-text" x="329" y="608.5" font-size="7.5" fill="#111" text-anchor="middle" font-weight="500">Start operation</text>
    </g>
  </svg>

  <nav class="sidebar" aria-label="Chart tools"></nav>
  <div class="btn" style="top:26px">Screen Shot</div>
  <div class="btn" style="top:70px">Heave Cancel</div>
  <div class="btn btn--active" style="top:117px">Prediction</div>
  <div class="btn" style="top:163px">Zoom</div>
  <div class="btn" style="top:209px">Snap Halo</div>
  <div class="btn" style="top:254px">Reset View</div>

  <div class="sidebar-low"></div>
  <div class="btn btn--tall" style="top:575px">Lock Hold<br>Period</div>
  <div class="btn btn--disabled" style="top:628px">Publish</div>
</body>
</html>
```